Stylish yet Funky Poster

We are a hair and beauty salon and have won some awards recently that we would like to display winning images in our window fronts.
Our windows are 900mm wide, 2100mm high. We have high res images and need to add some text somewhere on the image.
Salon colours are green, white though perhaps using black would be OK too.
I would like the text to read:-
2010 National Vello Shade Cup Winner
2010 Qld Vello Shade Cup Winner
(text as large as possible)

Model by Lou Parnell - (this text can be smaller)

The image is important but the more important purpose of the poster is to let passers by know about the competition wins.
Updates

Hi I've uploaded a new Dovria Logo which should be more clear.

I have uploaded bauhaus font also

Target Market(s)

Our target market are ladies 25 - 55 years old, mostly professional women.

Industry/Entity Type

Beauty Salon

Requirements
Must have
• Be 900mm wide, 2100mm high
• Must include supplied image.
• Must include text: 2010 National Vello Shade Cup Winner,
• 2010 Qld Vello Shade Cup Winner
• Model by Lou Parnell
Nice to have
• Salon name - Fernwick Hair & Beauty
• We also won 2008 National Vello Shade Cup too - this may be used on same banner
• Background can be changed
• Either black or white version of Dovria logo attached

```html
<!DOCTYPE html>
<html lang="en">
<head>
<meta charset="utf-8">
<title>Vello Shade Cup Winner Poster</title>
<link rel="stylesheet" href="https://fonts.googleapis.com/css2?family=Arimo:wght@400;700&family=Josefin+Sans:wght@100;200&display=swap">
<style>
  :root {
    --bg-light: #f4f4f4;
    --bg-mid: #e2e2e2;
    --ink-dark: #3b3b3d;
    --ink-grey: #5c5c5c;
    --rose: #b0676f;
    --rose-deep: #9a4f57;
    --rose-light: #d49aa0;
    --salon-green: #5b7b34;
    --hair: #6e1a2a;
    --hair-mid: #8a2a3a;
    --skin: #e8cfc2;
    --dress: #1f1f1f;
  }
  html, body {
    margin: 0;
    padding: 0;
    overflow: hidden;
  }
  body {
    width: 1200px;
    height: 2780px;
  }
  .poster {
    position: relative;
    width: 1200px;
    height: 2780px;
    overflow: hidden;
    background: radial-gradient(ellipse at 50% 45%, var(--bg-light) 0%, var(--bg-mid) 75%);
    font-family: "Arimo", Arial, sans-serif;
    text-align: center;
  }
  .credit {
    position: absolute;
    top: 74px;
    left: 0;
    width: 100%;
    margin: 0;
    font-size: 32px;
    font-weight: 700;
    letter-spacing: 6px;
    color: var(--ink-grey);
  }
  .credit .stylist {
    color: var(--salon-green);
  }
  .winning-photo {
    position: absolute;
    top: 140px;
    left: 0;
    width: 1200px;
    height: 1580px;
    background:
      radial-gradient(ellipse 22% 20% at 54% 26%, var(--skin) 0%, var(--skin) 55%, transparent 100%),
      radial-gradient(ellipse 34% 26% at 50% 20%, var(--hair-mid) 0%, var(--hair) 70%, transparent 100%),
      radial-gradient(ellipse 48% 30% at 52% 62%, var(--dress) 0%, #2e2e2e 55%, transparent 100%),
      radial-gradient(ellipse 40% 20% at 40% 40%, var(--skin) 0%, transparent 100%);
    -webkit-mask-image: radial-gradient(ellipse 60% 55% at 50% 45%, #000 65%, transparent 100%);
    mask-image: radial-gradient(ellipse 60% 55% at 50% 45%, #000 65%, transparent 100%);
  }
  .year {
    position: absolute;
    top: 1690px;
    left: 0;
    width: 100%;
    margin: 0;
    font-family: "Josefin Sans", Arial, sans-serif;
    font-weight: 100;
    font-size: 360px;
    line-height: 1;
    letter-spacing: 10px;
    color: var(--rose);
  }
  .national {
    position: absolute;
    top: 1965px;
    left: 0;
    width: 100%;
    margin: 0;
    font-size: 168px;
    font-weight: 700;
    line-height: 1;
    letter-spacing: -2px;
    color: var(--rose-deep);
    background: linear-gradient(180deg, var(--rose-light) 0%, var(--rose-deep) 100%);
    -webkit-background-clip: text;
    background-clip: text;
    -webkit-text-fill-color: transparent;
  }
  .winner {
    position: absolute;
    top: 2125px;
    left: 0;
    width: 100%;
    margin: 0;
    font-size: 165px;
    font-weight: 400;
    line-height: 1;
    letter-spacing: 2px;
    color: var(--ink-dark);
  }
  .awards {
    position: absolute;
    top: 2270px;
    left: 0;
    width: 100%;
    margin: 0;
    padding: 0;
    list-style: none;
  }
  .awards li {
    font-size: 102px;
    font-weight: 700;
    line-height: 105px;
    color: var(--salon-green);
  }
  .salon-name {
    position: absolute;
    top: 2615px;
    left: 0;
    width: 100%;
    display: flex;
    align-items: center;
    justify-content: center;
    gap: 18px;
    font-size: 36px;
    font-weight: 700;
    color: var(--salon-green);
  }
  .salon-name .mark {
    width: 34px;
    height: 34px;
    border-radius: 50%;
    background: var(--salon-green);
  }
</style>
</head>
<body>
  <main class="poster">
    <p class="credit">Model by <span class="stylist">Lou Parnell</span></p>
    <div class="winning-photo" role="img" aria-label="Award-winning portrait of a model with a burgundy red bob haircut wearing a black halter top with fabric flowers"></div>
    <p class="year">2010</p>
    <p class="national">National</p>
    <p class="winner">WINNER</p>
    <ul class="awards">
      <li>Qld Vello Shade Cup</li>
      <li>Vello Shade Cup</li>
    </ul>
    <div class="salon-name"><span class="mark"></span><span>Fernwick Hair &amp; Beauty</span></div>
  </main>
</body>
</html>
```